Lawn Maintenance Company needs Flyer (Postcard) Design.

Hi everyone.
The majority of what I do is lawn maintenance (grass cutting and trimming/edging).

I'm pretty well open to anything (even humour) but want to stay away from the cartoon/illustration type flyer (but always receptive if you think you have something that might look good, like Pipwren (Quillbys character) :)
Simple but I guess as everyone, something that catches people's eye.

Feel free to kind of play with the name if you think it would help, I would be willing to pay extra if you thought you had a good idea for some type of logo also.

Flyer/Postcard will be front and back, front mainly outlined here, back would be a list of additional services.

Main points I want to get across.
- Professional
- Reliable
- Not like the larger companies that send students or part time
helpers
Kind of want to get those points across without necessarily saying them.

Ok, well, if you haven't rolled your eyes and headed off to the next project.................... :)

Target Market(s)

Mostly regular people with bungalow / two storey houses that don't want to do it themselves and want a nice lawn to frame their house.

Industry/Entity Type

It Company

Requirements
Must have
• Front
** Brightfield Landscaping and Lawn Services
** Lawn Maintenance
** (416) 555-0382
** brightfieldyards@mailtrove.net

Back
Commercial and Residential
Plaza Maintenance
Spring/Fall Clean-up
Fertilizing
Weed Prevention
Hedge Trimming
Flower Bed Design
Topdressing
Triplemix
Overseeding
Lawn & flower bed re-edging
Eavestrough Cleaning
Nice to have
• ummmm....grass. lol :)
Birds
Butterflies
Should not have
• Elaborate homes/gardens
Pictures/photos of people

**The pictures I have included are to just give you an idea of the work I do and the type of properties I do**
Please let me know if you want more pics.

```html
<!DOCTYPE html>
<html lang="en">
<head>
<meta charset="utf-8">
<title>Brightfield Landscaping – Lawn Maintenance Flyer</title>
<link href="https://fonts.googleapis.com/css2?family=Montserrat:wght@600;700&family=Questrial&display=swap" rel="stylesheet">
<style>
  :root {
    --page-bg: #e4e4e4;
    --band-green: #1e8a17;
    --band-light: #5cbf24;
    --accent-yellow: #e2b923;
    --navy-top: #07145e;
    --navy-mid: #10289a;
    --sky-blue: #2450b8;
    --sky-pale: #dfe7f2;
    --grass-light: #49a81f;
    --grass-dark: #1c7410;
    --text-white: #ffffff;
  }
  * { margin: 0; padding: 0; box-sizing: border-box; }
  html, body {
    width: 1023px; height: 1200px; overflow: hidden;
    background: var(--page-bg);
  }
  .flyer {
    position: absolute; left: 110px; top: 0;
    width: 802px; height: 1200px; overflow: hidden;
    background: linear-gradient(180deg, var(--navy-top) 0%, var(--navy-mid) 28%, var(--sky-blue) 40%);
  }
  .top-band {
    position: absolute; left: 0; top: 0; width: 100%; height: 78px;
    background: linear-gradient(180deg, var(--band-green) 0%, var(--band-light) 55%, var(--band-green) 100%);
    border-bottom: 5px solid var(--accent-yellow);
  }
  .landscape {
    position: absolute; left: 0; top: 440px; width: 100%; height: 760px;
  }
  .landscape .sky {
    height: 405px;
    background: linear-gradient(180deg, rgba(36,80,184,0) 0%, #4f78c8 30%, #a9bde0 65%, var(--sky-pale) 100%);
  }
  .landscape .lawn {
    height: 355px;
    background: linear-gradient(180deg, var(--grass-light) 0%, #3a961a 45%, var(--grass-dark) 100%);
  }
  .company-name {
    position: absolute; left: 0; top: 240px; width: 100%;
    text-align: center;
    font-family: "Montserrat", sans-serif; font-weight: 600;
    font-size: 34px; line-height: 1.2;
    color: var(--text-white);
  }
  .service-title {
    position: absolute; left: 0; top: 334px; width: 100%;
    text-align: center;
    font-family: "Montserrat", sans-serif; font-weight: 700;
    font-size: 54px; line-height: 1; letter-spacing: 1px;
    color: var(--text-white);
  }
  .service-title .highlight { color: var(--accent-yellow); }
  .contact {
    position: absolute; left: 0; top: 1050px; width: 100%;
    text-align: center;
  }
  .contact .phone {
    font-family: "Questrial", sans-serif;
    font-size: 84px; line-height: 1;
    color: var(--text-white);
  }
  .contact .email {
    margin-top: 16px;
    font-family: "Montserrat", sans-serif; font-weight: 600;
    font-size: 25px; line-height: 1; letter-spacing: 1px;
    text-transform: uppercase;
    color: var(--accent-yellow);
  }
</style>
</head>
<body>
  <main class="flyer">
    <header class="top-band" role="img" aria-label="Green header band with decorative light green grass-blade swooshes"></header>

    <div class="landscape" role="img" aria-label="Photo of a bright blue sky with white clouds above a freshly mown striped green lawn">
      <div class="sky"></div>
      <div class="lawn"></div>
    </div>

    <h1 class="company-name">Brightfield Landscaping<br>and Lawn Services</h1>
    <h2 class="service-title"><span class="highlight">LAWN</span> MAINTENANCE</h2>

    <section class="contact">
      <p class="phone">(416) 555-0382</p>
      <p class="email">brightfieldyards@mailtrove.net</p>
    </section>
  </main>
</body>
</html>
```